Data Compass Plan- Brennal Insurance providing specialist Cyber and Liability Insurance

for Managed Technology Service Providers and their customer, we will use a letterhead that white labels insurer documents, which can be used in our physical letters as well as to be used within Email signatures.

Target Market(s)

Managed Technology Services Providers

Industry/Entity Type

Cyber Insurance

Requirements
Must have
• website, email address, contact phone numbers

```html
<!DOCTYPE html>
<html lang="en">
<head>
<meta charset="utf-8">
<title>Data Compass Plan – Letterhead and Business Card</title>
<link rel="stylesheet" href="https://fonts.googleapis.com/css2?family=Open+Sans:wght@400;600;700&display=swap">
<style>
  :root{
    --backdrop:#999999;
    --paper:#ffffff;
    --ink:#3d3d3d;
    --ink-soft:#555555;
    --charcoal:#444444;
    --green:#39b54a;
    --signature-tone:#e6e6e6;
  }
  *{margin:0;padding:0;box-sizing:border-box}
  html,body{width:1200px;height:866px;overflow:hidden}
  body{background:var(--backdrop);font-family:"Open Sans",Arial,sans-serif;color:var(--ink);position:relative}

  .letterhead{position:absolute;left:97px;top:92px;width:482px;height:681px;background:var(--paper);overflow:hidden}
  .card{position:absolute;left:632px;top:354px;width:472px;height:241px;background:var(--paper);overflow:hidden}

  .brand-name{position:absolute;font-weight:600;color:var(--charcoal);white-space:nowrap;letter-spacing:.2px}
  .letterhead .brand-name{left:32px;top:37px;font-size:17px;line-height:22px}
  .card .brand-name{left:22px;top:90px;font-size:19px;line-height:24px}

  .contact-list{position:absolute;list-style:none}
  .contact-list li{display:flex;align-items:center;white-space:nowrap}
  .contact-list svg{fill:var(--green);flex:none}
  .letterhead .contact-list{left:321px;top:31px;font-size:8px}
  .letterhead .contact-list li{height:11.5px;gap:4px}
  .letterhead .contact-list svg{width:7px;height:7px}
  .card .contact-list{left:280px;top:78px;font-size:11px}
  .card .contact-list li{height:15.2px;gap:5px}
  .card .contact-list svg{width:10px;height:10px}

  .card-divider{position:absolute;left:264px;top:83px;width:1px;height:40px;background:var(--green)}

  .recipient{position:absolute;left:32px;top:180px}
  .recipient-name{font-size:9.5px;line-height:13px;text-transform:uppercase;color:var(--ink)}
  .recipient-line{font-size:6.8px;line-height:11.8px;color:var(--ink-soft)}

  .letter-body{position:absolute;left:32px;top:240px;width:417px}
  .letter-body p{font-size:6.7px;line-height:11.7px;text-align:justify;color:var(--ink-soft);margin-bottom:10.5px}

  .sign-off{position:absolute;left:32px;top:428px;font-size:7.2px;color:var(--ink-soft)}
  .signature{position:absolute;left:32px;top:442px;width:88px;height:22px;background:var(--signature-tone);border-radius:2px}
  .signer-name{position:absolute;left:32px;top:470px;font-size:9px;color:var(--ink-soft)}

  .legal{position:absolute;left:0;width:100%;text-align:center;color:var(--ink)}
  .legal strong{font-weight:600}
  .legal .dot{color:var(--green);margin:0 6px}
  .legal .issuer{display:block}
  .letterhead .legal{top:628px;font-size:7.8px;line-height:12px}
  .letterhead .legal .issuer{font-size:6.6px}
  .card .legal{top:172px;font-size:11px;line-height:16px}
  .card .legal .issuer{font-size:9.2px}

  .footer-band{position:absolute;left:0;bottom:0;width:100%}
  .footer-band svg{display:block;width:100%;height:100%}
  .letterhead .footer-band{height:26px}
  .card .footer-band{height:34px}
  .footer-band .gray{fill:var(--charcoal)}
  .footer-band .green{fill:var(--green)}
  .web-address{position:absolute;color:#fff;font-weight:600;white-space:nowrap}
  .letterhead .web-address{right:13px;bottom:8px;font-size:9.4px}
  .card .web-address{right:21px;bottom:10px;font-size:12.4px}
</style>
</head>
<body>

<svg width="0" height="0" style="position:absolute" aria-hidden="true">
  <defs>
    <symbol id="icon-phone" viewBox="0 0 16 16"><path d="M3.6 1.2l2.3 2.6-1.3 1.8c.9 2 2.5 3.7 4.6 4.7l1.8-1.3 2.6 2.3-1.3 2.3C7 14.6 1.4 9 1.3 2.5z"/><path d="M10 1a5 5 0 0 1 5 5h-1.3A3.7 3.7 0 0 0 10 2.3zM10 3.6A2.4 2.4 0 0 1 12.4 6h-1.3A1.1 1.1 0 0 0 10 4.9z"/></symbol>
    <symbol id="icon-fax" viewBox="0 0 16 16"><path d="M4 1h6l2 2v3H4z"/><path d="M1 7h14v6h-3v2H4v-2H1zM5 11v3h6v-3z"/></symbol>
    <symbol id="icon-mail" viewBox="0 0 16 16"><path d="M1 3h14v1.5L8 9 1 4.5z"/><path d="M1 6.3l7 4.5 7-4.5V13H1z"/></symbol>
  </defs>
</svg>

<article class="letterhead">
  <div class="brand-name">Data Compass Plan</div>
  <ul class="contact-list">
    <li><svg><use href="#icon-phone"/></svg>303.555.0142</li>
    <li><svg><use href="#icon-fax"/></svg>303.555.0142</li>
    <li><svg><use href="#icon-mail"/></svg>info@DataCompassPlan.com</li>
  </ul>

  <div class="recipient">
    <div class="recipient-name">Darin Holloway</div>
    <div class="recipient-line">President / CEO</div>
    <div class="recipient-line">City/State, Zip Code</div>
  </div>

  <div class="letter-body">
    <p>Lorem Ipsum is simply dummy text of the printing and typesetting industry. Lorem Ipsum has been the industry's standard dummy text ever since the 1500s, when an unknown printer took a galley of type and scrambled it to make a type specimen book. It has survived not only five centuries, but also the leap into electronic typesetting, remaining essentially unchanged. It was popularised in the 1960s with the release of Letraset sheets containing Lorem Ipsum passages, and more recently with desktop publishing software like Aldus PageMaker including versions of Lorem Ipsum.</p>
    <p>It is a long established fact that a reader will be distracted by the readable content of a page when looking at its layout. The point of using Lorem Ipsum is that it has a more-or-less normal distribution of letters, as opposed to using 'Content here, content here', making it look like readable English. Many desktop publishing packages and web page editors now use Lorem Ipsum as their default model text, and a searchaccident, sometimes on purpose (injected humour and the like).</p>
    <p>There are many variations of passages of Lorem Ipsum available, but the majority have suffered alteration in some form, by injected humour, or randomised words which don't look even slightly believable. If you are going to use a passage of Lorem Ipsum, you need to be sure there isn't anything embarrassing hidden in the middle of text.</p>
  </div>

  <div class="sign-off">Sincerely,</div>
  <div class="signature" role="img" aria-label="Handwritten signature of Lena Marsh"></div>
  <div class="signer-name">Lena Marsh</div>

  <p class="legal"><strong>ABN no.</strong> 48 302 115 690<span class="dot">•</span><strong>Corporate Authorised Representative no.</strong> 1403326<span class="issuer">by Brennal Insurance</span></p>

  <div class="footer-band">
    <svg viewBox="0 0 482 26" preserveAspectRatio="none" aria-hidden="true">
      <polygon class="gray" points="0,6 306,6 298,11 0,11"/>
      <path class="green" d="M0 19 L300 19 C322 19 330 0 362 0 L482 0 L482 26 L0 26 Z"/>
    </svg>
  </div>
  <div class="web-address">www.DataCompassPlan.com</div>
</article>

<article class="card">
  <div class="brand-name">Data Compass Plan</div>
  <div class="card-divider"></div>
  <ul class="contact-list">
    <li><svg><use href="#icon-phone"/></svg>303.555.0142</li>
    <li><svg><use href="#icon-fax"/></svg>303.555.0142</li>
    <li><svg><use href="#icon-mail"/></svg>info@DataCompassPlan.com</li>
  </ul>

  <p class="legal"><strong>ABN no.</strong> 48 302 115 690<span class="dot">•</span><strong>Corporate Authorised Representative no.</strong> 1403326<span class="issuer">by Brennal Insurance</span></p>

  <div class="footer-band">
    <svg viewBox="0 0 472 34" preserveAspectRatio="none" aria-hidden="true">
      <polygon class="gray" points="0,9 237,9 224,16 0,16"/>
      <path class="green" d="M0 21 L214 21 C234 21 244 0 276 0 L472 0 L472 34 L0 34 Z"/>
    </svg>
  </div>
  <div class="web-address">www.DataCompassPlan.com</div>
</article>

</body>
</html>
```